B.S.L.H. Letterhead design

I would like a really professionally designed letterhead for my professional tutoring business called "The Bright Steps Learning Hub" (B.S.L.H.).Something fresh,modern and inspiring that will breath new life into the bu.The business/centre offers professional tutoring for 6 - 16 year olds in maths and english.

I have also attached a centre picture our logo, our proposed school bag,and our latest newsletter to give some perspective & background.

We like to see designs that use the blue & yellow colour theme.The final design should communicate ... "Giving Your Child A Secure Future ... And You Yourself ... Peace Of Mind!!!"

```html
<!DOCTYPE html>
<html lang="en">
<head>
<meta charset="utf-8">
<title>B.S.L.H. Letterhead</title>
<link rel="stylesheet" href="https://fonts.googleapis.com/css2?family=Arimo&family=Tenor+Sans&display=swap">
<style>
:root{
  --navy:#16306b;
  --gold:#f6c400;
  --ink:#575757;
  --paper:#ffffff;
  --ghost:#f3f3f3;
  --frame:#9a9a9a;
}
*{margin:0;padding:0;box-sizing:border-box}
html,body{width:849px;height:1200px;overflow:hidden;background:var(--paper)}
.letterhead{position:relative;width:849px;height:1200px;background:var(--paper);border-left:1px solid var(--frame);border-right:1px solid var(--frame);overflow:hidden}
.band{position:absolute;left:0;width:849px;display:block}
.band--top{top:0;height:160px}
.band--bottom{bottom:0;height:80px}
.brand{position:absolute;top:22px;left:0;width:849px;text-align:center;color:var(--gold);font-family:"Tenor Sans",sans-serif}
.brand__initials{display:inline-flex;align-items:center;gap:10px;font-size:34px;letter-spacing:2px;line-height:1;height:66px}
.brand__dot{width:14px;height:14px;border-radius:50%;background:var(--gold)}
.brand__site{font-size:17.5px;line-height:20px;margin-top:10px}
.brand__rule{width:222px;height:1px;background:var(--gold);margin:2px auto 3px}
.brand__tagline{font-size:9.5px;line-height:12px}
.backdrop{position:absolute;top:560px;left:0;width:849px;text-align:center;font-family:"Tenor Sans",sans-serif;font-size:150px;color:var(--ghost);letter-spacing:6px;line-height:1}
.letter{position:absolute;top:266px;left:98px;width:652px;font-family:"Arimo",sans-serif;font-size:16px;line-height:23.5px;color:var(--ink)}
.letter__salutation{margin-bottom:47px}
.letter p.body{text-align:justify;margin-bottom:23.5px}
.footer-name{position:absolute;top:1098px;left:0;width:849px;text-align:center;font-family:"Tenor Sans",sans-serif;font-size:16px;color:var(--navy)}
.footer-contact{position:absolute;top:1150px;left:0;width:849px;text-align:center;font-family:"Arimo",sans-serif;font-size:10.5px;line-height:16px;color:#ffffff}
</style>
</head>
<body>
<div class="letterhead">
  <svg class="band band--top" viewBox="0 0 849 160" preserveAspectRatio="none" aria-hidden="true">
    <path d="M0 0H849V58Q424.5 252 0 58Z" fill="var(--navy)"/>
  </svg>

  <header class="brand">
    <div class="brand__initials"><span class="brand__dot"></span>B.S.L.H.</div>
    <div class="brand__site">TheBrightStepsLearningHub.co.uk</div>
    <div class="brand__rule"></div>
    <div class="brand__tagline">London’s Leading Learning Centre</div>
  </header>

  <div class="backdrop" aria-hidden="true">B.S.L.H.</div>

  <main class="letter">
    <p class="letter__salutation">Dear Sir,</p>
    <p class="body">Lorem Ipsum is simply dummy text of the printing and typesetting industry. Lorem Ipsum has been the industry's standard dummy text ever since the 1500s, when an unknown printer took a galley of type and scrambled it to make a type specimen book. It has survived not only five centuries, but also the leap into electronic typesetting, remaining essentially unchanged. It was popularised in the 1960s with the release of Letrafix sheets containing Lorem Ipsum passages, and more recently with desktop publishing software like Folio PageDesk including versions of Lorem Ipsum.</p>
    <p class="body">Lorem Ipsum is simply dummy text of the printing and typesetting industry. Lorem Ipsum has been the industry's standard dummy text ever since the 1500s, when an unknown printer took a galley of type and scrambled it to make a type specimen book. It has survived not only five centuries, but also the leap into electronic typesetting, remaining essentially unchanged. It was popularised in the 1960s with the release of Letrafix sheets containing Lorem Ipsum passages, and more recently with desktop publishing software like Folio PageDesk including versions of Lorem Ipsum.</p>
    <p class="body">Lorem Ipsum is simply dummy text of the printing and typesetting industry. Lorem Ipsum has been the industry's standard dummy text ever since the 1500s, when an unknown printer took a galley of type and scrambled it to make a type specimen book.</p>
  </main>

  <div class="footer-name">The Bright Steps Learning Hub</div>

  <svg class="band band--bottom" viewBox="0 0 849 80" preserveAspectRatio="none" aria-hidden="true">
    <path d="M0 48Q424.5 -22 849 48V80H0Z" fill="var(--navy)"/>
  </svg>

  <footer class="footer-contact">
    <div>Add.:&nbsp; Your Commercial or office address • Ph.: 00.00.00.0000 • Fax: 00.00.00.0000</div>
    <div>Email: yourname@yourwebsite.com • Web.: www.yourwebsite.com</div>
  </footer>
</div>
</body>
</html>
```